WEB application for eBook purchasing

For private project, I have a plan to make WEB service that makes easy to purchase some or many books at once.

* Problem I want to solve
- I feel Brellow Tome shop is too poor to find books, especially for volumes of comics.

- That page on Brellow shows me many books but same title with different volumes.

- Check following links which shows same titles but many volumes:
- Japanese comic page. http://www.brellowshop.example.jp/b/ref=xq_link_11111111_1?ie=UTF8&node=1000000001&pf_rd_m=ZZ0000000000&pf_rd_s=left-1&pf_rd_r=00AAAA00AAAA00AAAA0A&pf_rd_t=101&pf_rd_p=100000001&pf_rd_i=1000000002
- Or think about Tobin Varga series.
http://www.brellowshop.example.com/s/ref=nb_sb_noss?url=search-alias%3Dstripbooks&field-keywords=Tobin+Varga

- If I don't have vol.1 of a comic, I must find the vol.1 in that page.

- And also I have vol.1 to 10 of the comic , I must find vol.11 in that pages.

- It's too annoying.

Target Market(s)

Brellow user who have frustrated Brellow Tome purchasing.

Industry/Entity Type

Store

Requirements
Must have
• * About format:
- html and scss/css are the best.
- FYI I develop client-side by AngularJS.
- if psd file comes, I have to buy Photoshop.

* Basically:
- Button to share this service for Chirpnest, Pallbook, or something.
- Search box to filter book title or author.
- Flat design

* Showcase page:
- Many beautiful cover pages of comic title.
- Shows how many volumes included and their total price on the cover page graphics.
- Shows detail page or box when a user touch the cover page graphics.

* Detail page or box:
- More detail of the comic (fetch from Lorepedium)
- All the cover pages for all volumes in a comic.
- Each price of volumes.
- Summary text of volumes (fetch from Brellow).
- Total price of selected volumes.
- User can select some or all the volumes then put them into Brellow cart.
- User can share this page by Chirpnest or something.

* Log in/out page or box:
- Username and password
- A user may connect via Chirpnest, Pallbook or the other social account.

* User profile page:
- Username and password change
- Purchase history.
Nice to have
• - I may want to extend this service for Novels, Music or Video purchasing and property management.
- So it's nice if I could have management for media type.

```html
<!DOCTYPE html>
<html lang="en">
<head>
<meta charset="utf-8">
<title>Shelfnook — Comic Series Store</title>
<link href="https://fonts.googleapis.com/css2?family=Open+Sans:wght@400;600;700&family=Oswald:wght@400;500&display=swap" rel="stylesheet">
<style>
:root{
  --ink:#222222;
  --text:#444444;
  --muted:#8a8a8a;
  --line:#dcdcdc;
  --panel:#f1f1f1;
  --white:#ffffff;
  --dark:#1b1b1b;
  --footer:#3a3a3a;
  --footer-text:#bdbdbd;
  --accent:#c0392b;
  --highlight:#dfe6ee;
}
*{box-sizing:border-box;margin:0;padding:0}
html,body{width:1200px;height:2360px;overflow:hidden}
body{font-family:"Open Sans",Arial,sans-serif;color:var(--text);background:var(--white);font-size:12px;position:relative}
.wrap{position:absolute;left:60px;width:1080px}

/* header */
.masthead{position:absolute;left:0;top:0;width:1200px;height:712px;background:var(--panel)}
.toplinks{position:absolute;right:60px;top:8px;font-size:10px;color:var(--muted)}
.toplinks span{margin-left:6px}
.logo{position:absolute;left:60px;top:22px;font-family:"Oswald",sans-serif;font-size:40px;font-weight:500;color:var(--ink);letter-spacing:1px}
.perks{position:absolute;left:500px;top:36px;display:flex;gap:26px}
.perk{display:flex;align-items:center;gap:8px;font-size:9px;line-height:12px;color:var(--text)}
.perk b{display:block;font-size:10px;color:var(--ink)}
.perk svg{flex:none}

.categories{position:absolute;left:60px;top:88px;width:240px;height:502px;background:var(--white);border:1px solid var(--line)}
.categories h3{height:36px;background:var(--dark);color:var(--white);font-size:12px;font-weight:600;padding:10px 12px;display:flex;justify-content:space-between}
.categories li{list-style:none;height:35px;line-height:35px;padding:0 14px;border-bottom:1px solid #ececec;font-size:12px;color:var(--text)}
.categories li.active{background:var(--highlight);color:var(--ink);font-weight:600}

.searchbar{position:absolute;left:320px;top:88px;width:820px;height:28px;display:flex;gap:6px}
.searchbar .cat{width:130px;background:var(--white);border:1px solid var(--line);font-size:10px;padding:6px 8px;display:flex;justify-content:space-between}
.searchbar .field{flex:1;background:var(--white);border:1px solid var(--line);font-size:10px;color:var(--muted);padding:6px 8px}
.searchbar .go{width:80px;background:var(--dark);color:var(--white);font-size:10px;font-weight:700;text-align:center;line-height:28px}
.searchbar .cart{width:120px;background:var(--dark);color:var(--white);font-size:10px;text-align:center;line-height:28px}

.hero{position:absolute;left:320px;top:124px;width:560px;height:388px;background:var(--white);border:1px solid var(--line)}
.hero .kicker{position:absolute;left:28px;top:26px;font-size:13px;color:var(--text)}
.hero .headline{position:absolute;left:28px;top:46px;font-size:26px;font-weight:700;color:var(--ink)}
.hero .art{position:absolute;left:40px;top:92px;width:380px;height:190px;border-radius:4px;background:linear-gradient(135deg,#d8443a,#f2c14e 40%,#3b8fd1 75%,#6cbf4f)}
.hero .shop{position:absolute;right:30px;top:240px;background:var(--dark);color:var(--white);font-size:10px;font-weight:700;padding:6px 12px}
.hero .thumbs{position:absolute;left:0;bottom:0;width:100%;height:96px;border-top:1px solid var(--line);display:flex}
.hero .thumbs div{flex:1;border-right:1px solid var(--line);padding:10px;display:flex;gap:8px;font-size:9px;line-height:12px}
.hero .thumbs div:last-child{border-right:0}
.hero .thumbs i{flex:none;width:50px;height:74px;background:linear-gradient(160deg,#5b7fb8,#c94f4f)}

.side-promo{position:absolute;left:896px;width:244px;height:190px;background:var(--white);border:1px solid var(--line)}
.side-promo .art{position:absolute;left:14px;top:16px;width:110px;height:150px;background:linear-gradient(150deg,#e5a63c,#b9472f)}
.side-promo p{position:absolute;left:136px;top:30px;width:96px;font-size:11px;line-height:15px}
.side-promo .price{position:absolute;left:136px;top:104px;font-size:16px;font-weight:700;color:var(--accent)}
.side-promo .shop{position:absolute;right:12px;bottom:14px;background:var(--dark);color:var(--white);font-size:9px;font-weight:700;padding:4px 8px}

.promo-row{position:absolute;left:320px;top:524px;width:820px;height:170px;display:flex;gap:12px}
.promo{flex:1;background:var(--white);border:1px solid var(--line);position:relative}
.promo .art{position:absolute;left:12px;top:14px;width:120px;height:140px;background:linear-gradient(160deg,#7a5fb0,#e06b8c)}
.promo p{position:absolute;left:144px;top:26px;width:110px;font-size:11px;line-height:15px}
.promo .price{position:absolute;left:144px;top:96px;font-size:16px;font-weight:700;color:var(--accent)}
.promo .shop{position:absolute;right:10px;bottom:12px;background:var(--dark);color:var(--white);font-size:9px;font-weight:700;padding:4px 8px}

/* newsletter */
.newsletter{top:732px;height:30px;background:var(--dark);display:flex;align-items:center;padding:0 12px;gap:14px}
.newsletter span{color:var(--white);font-size:11px;width:250px}
.newsletter .field{flex:1;height:20px;background:var(--white);font-size:10px;color:var(--muted);padding:3px 8px}
.newsletter .signup{color:var(--white);font-size:10px;font-weight:700;background:#444;padding:3px 12px}

/* series shelves */
.shelf{height:330px}
.shelf h2{font-size:20px;font-weight:600;color:var(--ink);height:30px;border-bottom:1px solid var(--line);display:flex;justify-content:space-between;align-items:center}
.shelf h2 small{font-size:11px;font-weight:400;color:var(--text)}
.cards{display:flex;gap:30px;margin-top:12px}
.series-card{width:192px;border:1px solid var(--line);height:282px;padding:10px;text-align:center}
.series-card.selected{border:2px solid var(--ink)}
.cover{position:relative;width:136px;height:180px;margin:0 auto}
.vol-count{position:absolute;left:0;bottom:0;background:rgba(0,0,0,.78);color:var(--white);font-size:9px;font-weight:700;padding:3px 6px}
.vol-total{position:absolute;right:0;bottom:0;background:var(--accent);color:var(--white);font-size:9px;font-weight:700;padding:3px 6px}
.series-card .title{font-size:11px;color:var(--ink);margin-top:8px;white-space:nowrap}
.series-card .prices{display:flex;justify-content:space-between;font-size:10px;margin-top:6px}
.series-card .prices s{color:var(--muted)}
.series-card .prices b{color:var(--ink)}
.series-card .prices em{font-style:normal;color:var(--accent)}
.select-vols{margin-top:8px;border:1px solid var(--line);font-size:9px;padding:4px;display:flex;align-items:center;justify-content:center;gap:5px;white-space:nowrap}
.arrow{position:absolute;width:30px;height:30px;border-radius:50%;background:#777;display:flex;align-items:center;justify-content:center}

.c1{background:linear-gradient(160deg,#c9302c,#f0c419)}
.c2{background:linear-gradient(160deg,#f06fa5,#7ed1e8)}
.c3{background:linear-gradient(160deg,#6d3fa0,#f2b134)}
.c4{background:linear-gradient(160deg,#3a6ac2,#e84a3c)}
.c5{background:linear-gradient(160deg,#2d7f5e,#c2d94f)}
.c6{background:linear-gradient(160deg,#e8c23a,#d6492f)}
.c7{background:linear-gradient(160deg,#5fb0e0,#2f4f8f)}

/* partners */
.partners-title{top:1898px;font-size:20px;font-weight:600;color:var(--ink);border-bottom:1px solid var(--line);height:30px}
.partners{top:1946px;height:70px;display:flex;justify-content:space-around;align-items:center;padding:0 60px}
.badge{width:90px;height:46px;background:#cfcfcf;border-radius:6px}
.badge.round{width:46px;border-radius:50%}

/* footer */
.footer{position:absolute;left:0;top:2050px;width:1200px;height:276px;background:var(--footer)}
.footer .cols{position:absolute;left:60px;top:24px;width:1080px;display:flex}
.footer .col{width:250px}
.footer h4{color:var(--white);font-size:11px;font-weight:700;margin-bottom:10px}
.footer li{list-style:none;color:var(--footer-text);font-size:10px;line-height:20px}
.footer .col.contact{width:330px}
.social{display:flex;gap:6px;margin-top:10px}
.social i{width:22px;height:22px;background:#5a5a5a}
.totop{position:absolute;right:24px;top:220px;width:40px;height:40px;border-radius:50%;background:var(--dark);display:flex;align-items:center;justify-content:center}
.bottombar{position:absolute;left:0;top:2326px;width:1200px;height:34px;background:#262626;color:var(--footer-text);font-size:9px}
.bottombar .left{position:absolute;left:60px;top:11px}
.bottombar .right{position:absolute;right:60px;top:11px}
</style>
</head>
<body>

<header class="masthead">
  <div class="toplinks"><span>Hi! Customer Support</span> | <span>Contact Us</span> | <span>Home</span> | <span>My Account</span> | <span>Wishlist</span> | <span>Login</span> | <span>Signup</span></div>
  <div class="logo">LOGO</div>
  <div class="perks">
    <div class="perk"><svg width="26" height="26" viewBox="0 0 26 26"><circle cx="13" cy="13" r="12" fill="#222"/><path d="M9 7l3 3-2 2c1 2 2 3 4 4l2-2 3 3-2 2c-5 0-10-5-10-10z" fill="#fff"/></svg><div><b>CALL US</b>021 555 0148</div></div>
    <div class="perk"><svg width="26" height="26" viewBox="0 0 26 26"><circle cx="13" cy="13" r="12" fill="#222"/><rect x="7" y="9" width="12" height="8" fill="#fff"/></svg><div><b>PAY ON DELIVERY</b>Cash on delivery</div></div>
    <div class="perk"><svg width="26" height="26" viewBox="0 0 26 26"><circle cx="13" cy="13" r="12" fill="#222"/><rect x="6" y="10" width="9" height="6" fill="#fff"/><rect x="15" y="12" width="5" height="4" fill="#fff"/></svg><div><b>FREE SHIPPING</b>Nationwide</div></div>
    <div class="perk"><svg width="26" height="26" viewBox="0 0 26 26"><circle cx="13" cy="13" r="12" fill="#222"/><rect x="8" y="12" width="10" height="7" fill="#fff"/><path d="M10 12v-2a3 3 0 016 0v2" stroke="#fff" stroke-width="1.6" fill="none"/></svg><div><b>SECURE WEBSITE</b>Encrypted connection</div></div>
  </div>

  <nav class="categories">
    <h3><span>All Categories</span><span>▾</span></h3>
    <ul>
      <li>Academic and Professional</li>
      <li>Biographies &amp; Autobiographies</li>
      <li>Branding and Management</li>
      <li>Coffee Table</li>
      <li>College Text &amp; Reference</li>
      <li>Comics &amp; Graphic Novels</li>
      <li>Computers &amp; Internet</li>
      <li>Entrance Exams Preparation</li>
      <li>Literature &amp; Fiction</li>
      <li class="active">Science &amp; Technology</li>
      <li>Teens</li>
      <li>Travel</li>
      <li>Other...</li>
    </ul>
  </nav>

  <div class="searchbar">
    <div class="cat"><span>Category</span><span>▾</span></div>
    <div class="field">Search by title or author</div>
    <div class="go">SEARCH</div>
    <div class="cart">My Shopping Cart</div>
  </div>

  <section class="hero">
    <div class="kicker">Lorem ipsum dolor sit amet consectetur</div>
    <div class="headline">Adipisicing elit</div>
    <div class="art" role="img" aria-label="Stack of colourful books"></div>
    <div class="shop">SHOP NOW</div>
    <div class="thumbs">
      <div><i role="img" aria-label="Book cover"></i><span>Lorem ipsum dolor sit</span></div>
      <div><i role="img" aria-label="Book cover"></i><span>Lorem ipsum dolor sit</span></div>
      <div><i role="img" aria-label="Book cover"></i><span>Lorem ipsum dolor sit</span></div>
      <div><i role="img" aria-label="Book cover"></i><span>Lorem ipsum dolor sit</span></div>
    </div>
  </section>

  <aside class="side-promo" style="top:124px">
    <div class="art" role="img" aria-label="Featured book cover"></div>
    <p>Lorem ipsum dolor sit amet consectetur</p>
    <div class="price">$24.99</div>
    <div class="shop">SHOP NOW</div>
  </aside>
  <aside class="side-promo" style="top:322px">
    <div class="art" role="img" aria-label="Featured book cover" style="background:linear-gradient(150deg,#4d8ad1,#2c3e70)"></div>
    <p>Lorem ipsum dolor sit amet consectetur</p>
    <div class="price">$24.99</div>
    <div class="shop">SHOP NOW</div>
  </aside>

  <div class="promo-row">
    <div class="promo"><div class="art" role="img" aria-label="Book cover"></div><p>Lorem ipsum dolor sit amet, adipiscing elit</p><div class="price">$24.99</div><div class="shop">SHOP NOW</div></div>
    <div class="promo"><div class="art" role="img" aria-label="Book cover" style="background:linear-gradient(160deg,#e0a23a,#8c3b2a)"></div><p>Lorem ipsum dolor sit amet, adipiscing elit</p><div class="price">$24.99</div><div class="shop">SHOP NOW</div></div>
    <div class="promo"><div class="art" role="img" aria-label="Book cover" style="background:linear-gradient(160deg,#3aa37a,#2a5f8c)"></div><p>Lorem ipsum dolor sit amet, adipiscing elit</p><div class="price">$24.99</div><div class="shop">SHOP NOW</div></div>
  </div>
</header>

<div class="wrap newsletter">
  <span>Become our VIP and receive daily deals</span>
  <div class="field">Enter your email here to join our mailing list</div>
  <div class="signup">SIGNUP</div>
</div>

<section class="wrap shelf" style="top:796px">
  <h2>Top New Releases in Books</h2>
  <div class="cards">
    <article class="series-card"><div class="cover c1" role="img" aria-label="Comic series cover"><span class="vol-count">12 VOLS</span><span class="vol-total">$89.40</span></div><div class="title">Lorem ipsum dolor sit amet</div><div class="prices"><s>$999</s><b>$899</b><em>50% Off</em></div><div class="select-vols">✓ Select volumes to add</div></article>
    <article class="series-card"><div class="cover c2" role="img" aria-label="Comic series cover"><span class="vol-count">8 VOLS</span><span class="vol-total">$59.60</span></div><div class="title">Lorem ipsum dolor sit amet</div><div class="prices"><s>$999</s><b>$899</b><em>50% Off</em></div><div class="select-vols">✓ Select volumes to add</div></article>
    <article class="series-card selected"><div class="cover c3" role="img" aria-label="Comic series cover"><span class="vol-count">24 VOLS</span><span class="vol-total">$178.80</span></div><div class="title">Lorem ipsum dolor sit amet</div><div class="prices"><s>$999</s><b>$899</b><em>50% Off</em></div><div class="select-vols">✓ Select volumes to add</div></article>
    <article class="series-card"><div class="cover c4" role="img" aria-label="Comic series cover"><span class="vol-count">15 VOLS</span><span class="vol-total">$111.75</span></div><div class="title">Lorem ipsum dolor sit amet</div><div class="prices"><s>$999</s><b>$899</b><em>50% Off</em></div><div class="select-vols">✓ Select volumes to add</div></article>
    <article class="series-card"><div class="cover c5" role="img" aria-label="Comic series cover"><span class="vol-count">6 VOLS</span><span class="vol-total">$44.70</span></div><div class="title">Lorem ipsum dolor sit amet</div><div class="prices"><s>$999</s><b>$899</b><em>50% Off</em></div><div class="select-vols">✓ Select volumes to add</div></article>
  </div>
</section>
<div class="arrow" style="left:40px;top:960px"><svg width="12" height="12" viewBox="0 0 12 12"><path d="M8 1L3 6l5 5" stroke="#fff" stroke-width="2" fill="none"/></svg></div>
<div class="arrow" style="left:1130px;top:960px"><svg width="12" height="12" viewBox="0 0 12 12"><path d="M4 1l5 5-5 5" stroke="#fff" stroke-width="2" fill="none"/></svg></div>

<section class="wrap shelf" style="top:1160px">
  <h2>Bestselling Books at shelfnook.com <small>View all &gt;&gt;</small></h2>
  <div class="cards">
    <article class="series-card"><div class="cover c6" role="img" aria-label="Comic series cover"><span class="vol-count">32 VOLS</span><span class="vol-total">$238.40</span></div><div class="title">Lorem ipsum dolor sit amet</div><div class="prices"><s>$999</s><b>$899</b><em>50% Off</em></div><div class="select-vols">✓ Select volumes to add</div></article>
    <article class="series-card"><div class="cover c4" role="img" aria-label="Comic series cover"><span class="vol-count">18 VOLS</span><span class="vol-total">$134.10</span></div><div class="title">Lorem ipsum dolor sit amet</div><div class="prices"><s>$999</s><b>$899</b><em>50% Off</em></div><div class="select-vols">✓ Select volumes to add</div></article>
    <article class="series-card"><div class="cover c7" role="img" aria-label="Comic series cover"><span class="vol-count">10 VOLS</span><span class="vol-total">$74.50</span></div><div class="title">Lorem ipsum dolor sit amet</div><div class="prices"><s>$999</s><b>$899</b><em>50% Off</em></div><div class="select-vols">✓ Select volumes to add</div></article>
    <article class="series-card"><div class="cover c2" role="img" aria-label="Comic series cover"><span class="vol-count">21 VOLS</span><span class="vol-total">$156.45</span></div><div class="title">Lorem ipsum dolor sit amet</div><div class="prices"><s>$999</s><b>$899</b><em>50% Off</em></div><div class="select-vols">✓ Select volumes to add</div></article>
    <article class="series-card"><div class="cover c3" role="img" aria-label="Comic series cover"><span class="vol-count">9 VOLS</span><span class="vol-total">$67.05</span></div><div class="title">Lorem ipsum dolor sit amet</div><div class="prices"><s>$999</s><b>$899</b><em>50% Off</em></div><div class="select-vols">✓ Select volumes to add</div></article>
  </div>
</section>

<section class="wrap shelf" style="top:1524px">
  <h2>Popular books <small>View all &gt;&gt;</small></h2>
  <div class="cards">
    <article class="series-card"><div class="cover c5" role="img" aria-label="Comic series cover"><span class="vol-count">40 VOLS</span><span class="vol-total">$298.00</span></div><div class="title">Lorem ipsum dolor sit amet</div><div class="prices"><s>$999</s><b>$899</b><em>50% Off</em></div><div class="select-vols">✓ Select volumes to add</div></article>
    <article class="series-card"><div class="cover c1" role="img" aria-label="Comic series cover"><span class="vol-count">14 VOLS</span><span class="vol-total">$104.30</span></div><div class="title">Lorem ipsum dolor sit amet</div><div class="prices"><s>$999</s><b>$899</b><em>50% Off</em></div><div class="select-vols">✓ Select volumes to add</div></article>
    <article class="series-card"><div class="cover c6" role="img" aria-label="Comic series cover"><span class="vol-count">27 VOLS</span><span class="vol-total">$201.15</span></div><div class="title">Lorem ipsum dolor sit amet</div><div class="prices"><s>$999</s><b>$899</b><em>50% Off</em></div><div class="select-vols">✓ Select volumes to add</div></article>
    <article class="series-card"><div class="cover c7" role="img" aria-label="Comic series cover"><span class="vol-count">11 VOLS</span><span class="vol-total">$81.95</span></div><div class="title">Lorem ipsum dolor sit amet</div><div class="prices"><s>$999</s><b>$899</b><em>50% Off</em></div><div class="select-vols">✓ Select volumes to add</div></article>
    <article class="series-card"><div class="cover c4" role="img" aria-label="Comic series cover"><span class="vol-count">7 VOLS</span><span class="vol-total">$52.15</span></div><div class="title">Lorem ipsum dolor sit amet</div><div class="prices"><s>$999</s><b>$899</b><em>50% Off</em></div><div class="select-vols">✓ Select volumes to add</div></article>
  </div>
</section>

<h2 class="wrap partners-title">Our Company</h2>
<div class="wrap partners">
  <div class="badge round"></div>
  <div class="badge"></div>
  <div class="badge"></div>
  <div class="badge round"></div>
  <div class="badge"></div>
  <div class="badge round"></div>
</div>
<div class="arrow" style="left:70px;top:1966px;background:none"><svg width="14" height="14" viewBox="0 0 12 12"><path d="M8 1L3 6l5 5" stroke="#555" stroke-width="2" fill="none"/></svg></div>
<div class="arrow" style="left:1100px;top:1966px;background:none"><svg width="14" height="14" viewBox="0 0 12 12"><path d="M4 1l5 5-5 5" stroke="#555" stroke-width="2" fill="none"/></svg></div>

<footer class="footer">
  <div class="cols">
    <div class="col"><h4>INFORMATION</h4><ul><li>About Shop</li><li>Customer Service</li><li>Customer Assistance</li><li>Privacy Policy</li><li>Terms &amp; Condition</li><li>Wholesale Delivery</li></ul></div>
    <div class="col"><h4>SHIPPING &amp; SUPPORT</h4><ul><li>International Shipping</li><li>Orders and Returns</li><li>Delivery Information</li><li>Secure Shopping</li></ul></div>
    <div class="col"><h4>MY ACCOUNT</h4><ul><li>My Account</li><li>Order History</li><li>New Collection</li><li>Wish List</li><li>Newsletter</li></ul></div>
    <div class="col contact"><h4>CONTACT US</h4><ul><li>12 Elm Row, Harbor District, 2048 New Town</li><li>hello@shelfnook.com</li><li>orders@shelfnook.com</li><li>021 555 0148</li><li>021 555 0192</li></ul>
      <div class="social" aria-label="Share buttons"><i></i><i></i><i></i><i></i><i></i></div></div>
  </div>
  <div class="totop"><svg width="16" height="16" viewBox="0 0 16 16"><path d="M3 11l5-5 5 5" stroke="#fff" stroke-width="2.4" fill="none"/></svg></div>
</footer>
<div class="bottombar">
  <span class="left">Copyright 2013 shelfnook.com All rights reserved</span>
  <span class="right">Delivery &amp; Returns | Terms &amp; Conditions | Site Map | Help</span>
</div>

</body>
</html>
```